*** Business Card Design Project

As a starting point, please take a look at our website www.plentarohire.com as a starting point.

We are looking for you to design our new business cards for plentarohire, something funky, cool and potentially unusual/different.

Good luck.

Industry/Entity Type

Business

```html
<!DOCTYPE html>
<html lang="en">
<head>
<meta charset="utf-8">
<title>plentarohire business card</title>
<link rel="stylesheet" href="https://fonts.googleapis.com/css2?family=PT+Sans:wght@400;700&display=swap">
<style>
  :root {
    --page-bg: #e9e6e1;
    --card-light: #fbfbfb;
    --card-mid: #e4e5e8;
    --band-light: #f6f3ee;
    --band-edge: #d9d6d2;
    --ink: #3b3d44;
    --ink-soft: #6d7079;
    --accent: #ef7a1a;
    --icon-bg: #5b6f93;
  }
  * { box-sizing: border-box; margin: 0; padding: 0; }
  html, body {
    width: 1200px; height: 1023px; overflow: hidden;
    background: var(--page-bg);
    font-family: "PT Sans", sans-serif;
  }
  .card {
    position: absolute; left: 100px; top: 225px;
    width: 1000px; height: 572px;
    background: linear-gradient(160deg, var(--card-light) 0%, var(--card-mid) 100%);
    box-shadow: 0 18px 40px rgba(60, 45, 30, 0.25);
    overflow: hidden;
  }
  .band {
    position: absolute; top: 0; bottom: 0; left: 300px; width: 110px;
    background: linear-gradient(90deg, var(--band-edge) 0%, var(--band-light) 20%, var(--band-light) 80%, var(--band-edge) 100%);
    opacity: 0.85;
  }
  .brand {
    position: absolute; left: 70px; top: 70px;
    display: flex; align-items: center; gap: 16px;
  }
  .brand-dot {
    width: 46px; height: 46px; border-radius: 50%;
    background: var(--accent);
  }
  .brand-name {
    font-size: 50px; font-weight: 700; color: var(--ink);
    letter-spacing: 1px; line-height: 1;
  }
  .brand-tagline {
    position: absolute; left: 300px; top: 128px;
    font-size: 18px; color: var(--ink-soft); letter-spacing: 1px;
  }
  .brand-rule {
    position: absolute; left: 0; top: 160px; width: 620px; height: 3px;
    background: linear-gradient(90deg, var(--accent) 0%, var(--accent) 60%, rgba(239,122,26,0) 100%);
  }
  .contact-list {
    position: absolute; left: 90px; top: 225px;
    list-style: none;
  }
  .contact-item {
    display: flex; align-items: center; gap: 16px;
    height: 40px; font-size: 20px; color: var(--ink);
  }
  .contact-icon {
    width: 24px; height: 24px; flex: none;
  }
  .social-mark {
    width: 24px; height: 18px; flex: none;
    background: var(--icon-bg); border-radius: 2px;
  }
</style>
</head>
<body>
  <div class="card">
    <div class="band"></div>

    <div class="brand">
      <span class="brand-dot"></span>
      <span class="brand-name">plentarohire</span>
    </div>
    <div class="brand-tagline">Executive Search</div>
    <div class="brand-rule"></div>

    <ul class="contact-list">
      <li class="contact-item">
        <svg class="contact-icon" viewBox="0 0 24 24"><circle cx="12" cy="12" r="11" fill="none" stroke="#5b6f93" stroke-width="1.5"/><path d="M12 6a4 4 0 0 0-4 4c0 3 4 8 4 8s4-5 4-8a4 4 0 0 0-4-4z" fill="#5b6f93"/><circle cx="12" cy="10" r="1.5" fill="#fff"/></svg>
        <span>14 - 16 Larkfield Row London EC2A 4PL</span>
      </li>
      <li class="contact-item">
        <svg class="contact-icon" viewBox="0 0 24 24"><circle cx="12" cy="12" r="11" fill="none" stroke="#5b6f93" stroke-width="1.5"/><rect x="6" y="8" width="12" height="8" fill="none" stroke="#5b6f93" stroke-width="1.5"/><path d="M6 8l6 5 6-5" fill="none" stroke="#5b6f93" stroke-width="1.5"/></svg>
        <span>info@plentarohire.com</span>
      </li>
      <li class="contact-item">
        <svg class="contact-icon" viewBox="0 0 24 24"><circle cx="12" cy="12" r="11" fill="none" stroke="#5b6f93" stroke-width="1.5"/><path d="M8 6.5l2 .5 1 3-1.5 1a7 7 0 0 0 3.5 3.5l1-1.5 3 1 .5 2c-1 1.5-3 1.5-5 .5a11 11 0 0 1-5-5c-1-2-1-4 .5-5z" fill="#5b6f93"/></svg>
        <span>+44 203 555 0147</span>
      </li>
      <li class="contact-item">
        <span class="social-mark"></span>
        <span>www.proflink.net/company/2047311</span>
      </li>
      <li class="contact-item">
        <span class="social-mark"></span>
        <span>www.friendpage.net/pages/PH-Executive-Search/204731158820</span>
      </li>
      <li class="contact-item">
        <span class="social-mark"></span>
        <span>chat username</span>
      </li>
      <li class="contact-item">
        <span class="social-mark"></span>
        <span>www.chirpline.net/plentarohire_ex</span>
      </li>
    </ul>
  </div>
</body>
</html>
```